Corporate Business Card

Very professional, Modern, Not to busy, include phone address email, website
(253) 555-0174, 61807 19th Street N, Kent, WA 98517, marcus@kestrelbayholding.com, brelvanindustries.com

Target Market(s)

Manufacturing

Industry/Entity Type

Aero, machining, manufacturing, Off road racing

Contact Information for Business Card

Phone, address email, website

```html
<!DOCTYPE html>
<html lang="en">
<head>
<meta charset="utf-8">
<title>Brelvan Industries – Business Card</title>
<link rel="stylesheet" href="https://fonts.googleapis.com/css2?family=Arimo:wght@400;700&family=Michroma&display=swap">
<style>
  :root {
    --page-bg: #e4e4e2;
    --card-bg: #3a3a3a;
    --card-panel: #444444;
    --card-panel-soft: #4a4a4a;
    --brand-red: #d0161b;
    --ink-light: #ffffff;
    --ink-muted: #e6e6e6;
    --shadow: rgba(0, 0, 0, 0.28);
  }
  * { box-sizing: border-box; margin: 0; padding: 0; }
  html, body {
    width: 1200px; height: 801px; overflow: hidden;
    background: var(--page-bg);
    font-family: "Arimo", Arial, sans-serif;
  }
  .sheet { position: relative; width: 1200px; height: 801px; }

  .card {
    position: absolute;
    width: 520px; height: 297px;
    background: var(--card-bg);
    box-shadow: 0 12px 28px var(--shadow);
    overflow: hidden;
  }
  .card--front { left: 50px; top: 252px; }
  .card--back  { left: 630px; top: 252px; }

  .card__panels { position: absolute; inset: 0; }

  .brand {
    position: absolute;
    display: flex; align-items: center; gap: 10px;
    font-family: "Michroma", "Arimo", sans-serif;
    color: var(--ink-light);
    letter-spacing: 0.5px;
    white-space: nowrap;
  }
  .brand__mark { width: 12px; height: 12px; background: var(--brand-red); }
  .card--front .brand { left: 30px; top: 44px; font-size: 19px; }
  .card--back .brand { left: 120px; top: 150px; font-size: 22px; }

  .rule { position: absolute; height: 2px; background: var(--ink-light); }
  .card--front .rule { left: 30px; top: 92px; width: 190px; }
  .card--back .rule  { left: 120px; top: 200px; width: 200px; }

  .person { position: absolute; left: 30px; top: 118px; }
  .person__name { color: var(--brand-red); font-size: 17px; letter-spacing: 0.5px; }
  .person__role { color: var(--ink-light); font-size: 13px; margin-top: 3px; }

  .contact { position: absolute; left: 30px; top: 176px; list-style: none; }
  .contact__item {
    display: flex; align-items: center; gap: 9px;
    color: var(--ink-light); font-size: 12.5px; line-height: 22px;
  }
  .contact__icon { width: 12px; height: 12px; flex: none; }

  .address {
    position: absolute; right: 30px; top: 104px;
    color: var(--ink-muted); font-size: 12.5px; line-height: 18px;
    text-align: right; font-style: normal;
  }

  .edge-tab {
    position: absolute; left: 0; top: 180px;
    width: 6px; height: 26px; background: var(--brand-red);
  }
  .edge-band { position: absolute; bottom: 0; height: 8px; }
  .edge-band--red { left: 0; width: 330px; background: var(--brand-red); }
  .edge-band--white { left: 330px; right: 0; background: var(--ink-light); }
</style>
</head>
<body>
<main class="sheet">

  <section class="card card--front" aria-label="Business card front">
    <svg class="card__panels" width="520" height="297" viewBox="0 0 520 297" aria-hidden="true">
      <polygon points="250,60 470,60 470,110 300,230 250,230" fill="var(--card-panel)"/>
      <polygon points="340,180 520,60 520,130 390,230 340,230" fill="var(--card-panel-soft)"/>
      <rect x="20" y="108" width="240" height="170" rx="22" fill="var(--card-panel)"/>
    </svg>

    <div class="brand"><span class="brand__mark"></span>Brelvan Industries</div>
    <div class="rule"></div>

    <div class="person">
      <div class="person__name">DANIEL REYES</div>
      <div class="person__role">Manager</div>
    </div>

    <ul class="contact">
      <li class="contact__item">
        <svg class="contact__icon" viewBox="0 0 12 12" aria-hidden="true"><path d="M2.5 1 L4.5 1 L5.2 3.6 L4 4.6 Q5.2 7 7.4 8 L8.4 6.8 L11 7.5 L11 9.5 Q10.5 11 9 11 Q1 10 1 2.5 Q1 1 2.5 1Z" fill="var(--brand-red)"/></svg>
        (253) 555-0174
      </li>
      <li class="contact__item">
        <svg class="contact__icon" viewBox="0 0 12 12" aria-hidden="true"><rect x="0.5" y="2" width="11" height="8" fill="var(--brand-red)"/><path d="M0.5 2 L6 6.5 L11.5 2" stroke="var(--card-bg)" stroke-width="1" fill="none"/></svg>
        marcus@kestrelbayholding.com
      </li>
      <li class="contact__item">
        <svg class="contact__icon" viewBox="0 0 12 12" aria-hidden="true"><circle cx="6" cy="6" r="5.2" fill="none" stroke="var(--brand-red)" stroke-width="1.4"/><path d="M1 6 H11 M6 1 Q3 6 6 11 M6 1 Q9 6 6 11" stroke="var(--brand-red)" stroke-width="1" fill="none"/></svg>
        www.brelvanindustries.com
      </li>
    </ul>

    <address class="address">61807 19th Street N<br>Kent, WA 98517</address>

    <div class="edge-tab"></div>
    <div class="edge-band edge-band--red"></div>
    <div class="edge-band edge-band--white"></div>
  </section>

  <section class="card card--back" aria-label="Business card back">
    <svg class="card__panels" width="520" height="297" viewBox="0 0 520 297" aria-hidden="true">
      <defs>
        <linearGradient id="backBand" x1="0" y1="0" x2="1" y2="0">
          <stop offset="0" stop-color="#2a2a2a"/>
          <stop offset="0.6" stop-color="#6e6e6e"/>
          <stop offset="1" stop-color="#4e4e4e"/>
        </linearGradient>
      </defs>
      <rect x="0" y="0" width="95" height="297" fill="url(#backBand)" opacity="0.85"/>
    </svg>

    <div class="brand"><span class="brand__mark"></span>Brelvan Industries</div>
    <div class="rule"></div>
  </section>

</main>
</body>
</html>
```